3 Politically Incorrect Greeting Cards

I would like to see some clean, colorful, and modern designs for 3 "politically incorrect" greeting cards aimed at young, single, successful women. I would like them to say:

Card 1: " Congratulations on not marrying the wrong person"
Card 2: " Congratulations on buying a house without a husband"
Card 3: " Thank you for not forgetting about me now that you have a boyfriend"

My initial thought was to have a white background with simple black writing, but I think a colorful background with a white text box in the middle might be more appropriate. I can't imagine the cards having any images/icons on them, but I'm open to suggestions if you think it would improve on the design. You guys are likely more creative than I am.

I've included a couple pics of looks I like - but like I said - I'm open to suggestions and what I like may not be appropriate for these cards. All the cards can have a similar esthetic or theme (maybe the same fonts but different colors or different color florals in each) or they can be completely different.

Target Market(s)

Young, single, successful women mid-20s to mid 40's.

Font styles to use
Serif
Sans Serif
Other font styles liked:
• Watercolour lettering maybe

Colors

Designer to choose colors to be used in the design.

Requirements
Must have
• Clean, colorful, bright, professional looking. The right tone for the message.
• I think the message is bold so the writing and colors have to be as well. I have included examples of ideas I like.
Nice to have
• Images, illustrations, icons, maybe patterns or some decorative details. Something to make the card more interesting than just the words (like the blue background with black letters one I made). I like a bright pattern with a white box in the center with the text.
Should not have
• Special effects, galaxy pictures, ugly images, bland colors.

```html
<!DOCTYPE html>
<html lang="en">
<head>
<meta charset="utf-8">
<title>Greeting Card Set</title>
<link rel="stylesheet" href="https://fonts.googleapis.com/css2?family=Noto+Sans:wght@400&family=Fira+Sans+Condensed:ital@1&display=swap">
<style>
  :root {
    --page: #ffffff;
    --stone: #e9e5e1;
    --mint: #bcf8d3;
    --sky: #c9eff5;
    --ink: #1f2a2e;
    --ink-soft: #4a5558;
  }
  * { margin: 0; padding: 0; box-sizing: border-box; }
  html, body { width: 1200px; height: 1200px; overflow: hidden; background: var(--page); }
  .card-strip {
    position: absolute;
    left: 359px; top: 54px;
    width: 498px; height: 1084px;
    display: flex; flex-direction: column;
  }
  .card {
    flex: 1;
    display: flex; align-items: center; justify-content: center;
  }
  .card--stone { background: var(--stone); }
  .card--mint { background: var(--mint); }
  .card--sky { background: var(--sky); }
  .message {
    width: 340px;
    text-align: center;
    padding: 14px 0 15px;
    background: radial-gradient(ellipse at center, rgba(255,255,255,0.7) 0%, rgba(255,255,255,0.35) 55%, rgba(255,255,255,0) 100%);
  }
  .message--wide { width: 360px; }
  .message__title {
    font-family: "Noto Sans", sans-serif;
    font-weight: 400;
    font-size: 21px;
    letter-spacing: 1px;
    color: var(--ink);
    line-height: 1.1;
  }
  .message__title--wide { letter-spacing: 4px; }
  .message__line {
    font-family: "Fira Sans Condensed", sans-serif;
    font-style: italic;
    font-weight: 400;
    font-size: 12px;
    letter-spacing: 1.2px;
    color: var(--ink-soft);
    line-height: 1.2;
    margin-top: 1px;
    white-space: nowrap;
  }
  .message__line--tight { letter-spacing: 0.8px; }
</style>
</head>
<body>
  <main class="card-strip">
    <section class="card card--stone">
      <div class="message">
        <h2 class="message__title">CONGRATULATIONS</h2>
        <p class="message__line">on not marrying the wrong person</p>
      </div>
    </section>
    <section class="card card--mint">
      <div class="message">
        <h2 class="message__title">CONGRATULATIONS</h2>
        <p class="message__line">on buying a house without a husband</p>
      </div>
    </section>
    <section class="card card--sky">
      <div class="message message--wide">
        <h2 class="message__title message__title--wide">THANK YOU</h2>
        <p class="message__line message__line--tight">for not forgetting about me now that you have a boyfriend</p>
      </div>
    </section>
  </main>
</body>
</html>
```